Surviving Domestic Violence Flyer

I need a flyer that "POPS" to attract participants for my research project. I have added the important information on my draft flyer.

```html
<!DOCTYPE html>
<html lang="en">
<head>
<meta charset="utf-8">
<title>Perceived Effectiveness of Domestic Violence Services</title>
<link rel="stylesheet" href="https://fonts.googleapis.com/css2?family=Bebas+Neue&family=Roboto+Condensed:ital,wght@1,700&display=swap">
<style>
  :root {
    --ink: #0c0e0e;
    --ink-soft: #1a1c1c;
    --white: #ffffff;
    --grey: #d6d6d6;
    --muted: #b9b9b9;
    --red: #e4161c;
    --red-bright: #f0222a;
    --red-deep: #6d0508;
  }
  * { box-sizing: border-box; margin: 0; padding: 0; }
  html, body {
    width: 928px; height: 1200px; overflow: hidden; background: var(--ink);
  }
  .flyer {
    position: relative; width: 928px; height: 1200px; overflow: hidden;
    background: linear-gradient(180deg, var(--ink-soft) 0%, var(--ink) 60%, #0a0c0c 100%);
    font-family: Arial, Helvetica, sans-serif; color: var(--white);
  }
  .hero-photo {
    position: absolute; left: 0; top: 0; width: 928px; height: 560px;
    background:
      radial-gradient(ellipse 55% 60% at 50% 28%, #8a8a8a 0%, #4c4c4c 45%, rgba(20,22,22,0) 80%),
      linear-gradient(180deg, #2e2e2e 0%, #1b1d1d 70%, rgba(26,28,28,0) 100%);
  }
  .title {
    position: absolute; left: 58px; top: 322px; width: 812px;
    font-family: "Bebas Neue", Impact, sans-serif; font-weight: 400;
    font-size: 90px; line-height: 84px; letter-spacing: 0.4px; white-space: nowrap;
    -webkit-text-stroke: 1.5px currentColor;
    text-shadow: 2px 3px 4px rgba(0,0,0,.8);
  }
  .title .accent { color: var(--red); }
  .questions {
    position: absolute; left: 58px; top: 544px; width: 830px; list-style: none;
    font-family: "Bebas Neue", Impact, sans-serif; font-size: 37px; line-height: 44px;
    color: var(--grey); letter-spacing: 0.5px; white-space: nowrap;
    -webkit-text-stroke: 0.6px currentColor;
    text-shadow: 1px 2px 3px #000;
  }
  .questions .you, .questions .mark { color: var(--red); }
  .eligibility {
    position: absolute; left: 58px; top: 820px; width: 830px;
    font-family: "Roboto Condensed", "Arial Narrow", sans-serif;
    font-size: 19.5px; line-height: 26px; font-weight: 700; font-style: italic; color: var(--white);
  }
  .contact-box {
    position: absolute; left: 56px; top: 917px; width: 812px; height: 102px;
    border: 1.5px solid var(--white);
    background: linear-gradient(180deg, var(--red-bright) 0%, #c80f14 45%, var(--red-deep) 100%);
    text-align: center; font-weight: bold; font-size: 26px; line-height: 38px; padding-top: 12px;
  }
  .contact-box .phone { font-size: 33px; }
  .compensation {
    position: absolute; left: 0; top: 1034px; width: 928px; text-align: center;
    font-family: "Bebas Neue", Impact, sans-serif; font-size: 50px; line-height: 56px;
    letter-spacing: 0.3px; color: var(--white);
    -webkit-text-stroke: 1px currentColor;
  }
  .credits {
    position: absolute; left: 0; top: 1106px; width: 928px; text-align: center;
    font-size: 13px; line-height: 17px; color: var(--muted);
  }
</style>
</head>
<body>
<main class="flyer">
  <div class="hero-photo" role="img" aria-label="Dramatic black and white photograph of a frightened woman with red bruise marks, a hand covering her mouth"></div>

  <h1 class="title">
    <span class="accent">Perceived</span> Effectiveness of<br>
    <span class="accent">Domestic Violence</span> Services
  </h1>

  <ul class="questions">
    <li>Are <span class="you">you</span> eighteen years of age or older <span class="mark">?</span></li>
    <li>Have <span class="you">you</span> been a victim &nbsp;of domestic voilonce <span class="mark">?</span></li>
    <li>Have <span class="you">you</span> sought assistance with abuse in the last 12 months <span class="mark">?</span></li>
    <li>Are <span class="you">you</span> still in contact with the person who abuse you <span class="mark">?</span></li>
    <li>Are <span class="you">you</span> willing and open to &nbsp;discussing your experience with<br>abuse and your attempts to access services or resources <span class="mark">?</span></li>
  </ul>

  <p class="eligibility">If you answered yes to all questions, you may be eligible to participate to better understand<br>the resources needed and services expected for survivors of domestic violence.</p>

  <div class="contact-box">
    Please contact Dana Whitfield at <span class="phone">1(555)014-2290</span><br>
    or via e-mail: survivorvoicesstudy@example.org
  </div>

  <p class="compensation">Participants will be compesated of their time</p>

  <div class="credits">
    <p>Principal Ivestigator: Dana Whitfield</p>
    <p>Institutional Affiliation: Lakeshore State University, Dept. of Criminology, Low and Justice</p>
    <p>Contact Address: Post Office Box 55021, Riverton, IL, 60612</p>
  </div>
</main>
</body>
</html>
```